Velquora - Label design for a supplement with probiotic and prebiotic

Hello, we are a supplement company and we need a label design for our first product. The product's name is Velquora and the company's name is Toskarend Nutrition (Logo attached, It is allowed to change the color) and we are located in Orlando, if we like the label, in the future we can make other products too.
Our product is a supplement that contains probiotics, prebiotics and other vitamins, it will be packaged in a 300g plastic jar (Img attached), we like simple but premium-looking packaging.
Below are some links to brands and products we like:
https://www.brelvomarket.example/stores/page/5D2811AC-9182-4E3A-B204-C7E613ABC1DE?ingress=2&visitId=81d3eab2-1c7f-4b2e-9a01-c3f5e2d7a614&ref_=bl_dp_s_web_28351704822
https://www.brelvomarket.example/stores/page/71AB3E9D-62C4-4B17-93AA-5DE208153B81?ingress=2&visitId=6519e7ab-204c-4d8e-b3f1-7a2c90d4e1f3&ref_=bl_dp_s_web_24719032855
https://www.brelvomarket.example/stores/Quillden+Nutrition/page/C2819043-7E61-4B35-91D4-28817C03E59A?store_ref=SLP_FW_438E21DA-B91C-4A56-C88B-5213A7F0C6E2
https://www.brelvomarket.example/stores/page/EE4A17BD-29C3-4D11-A572-6BCCFA38419D?ingress=2&visitId=19b3e702-4a5d-4f8c-bd21-c8e304a7d916&ref_=bl_dp_s_web_8412093577
https://www.brelvomarket.example/stores/node/29374015822?_encoding=UTF8&field-lbr_brands_browse-bin=GLOWPATHNUTRITION&ref_=bl_dp_s_web_29374015822
https://www.brelvomarket.example/stores/page/526FA184-3307-4C29-B7D1-E9A3C28B06F1?ingress=6&visitId=4a19c6d3-8e27-4b01-a5f3-1d6b93e7c024&store_ref=storeRecs_Instant_27319388144
Hi, This product will be packaged in a 300g bottle, it is allowed to insert images and it is very important to inform "100 Billion live bacteria", 5 grams of probiotic, 5 grams of prebiotic and orange flavor.
The bottle is rounded, the size of the art must be 2.87 in and 10.74 in, I will need barcode space, supplement facts, directions and warning. This information I can put later.
Target Market(s)
Our target is people who wish to have a healthier recovery after undergoing cancer treatments, helping to maintain health, improving quality of life and reducing the harm that these treatments cause.
Requirements
Must have
- It is very important that the product contains the following information:
- 100 Billion live bacteria
- 5 grams of probiotic and 5 grams of prebiotic
- No artificial flavours
- Space for barcode
Amount per container: 10.6 oz (300 g)
Serving size: 1 scoop (10 grams)
Servings per container: 30
Amount per serving
Calories 15 Calories from fat 0
Total Fat 0
Total Carbohydrate 5g
Dietary fiber 4g
Sugars 1g
Protein 0g
Proprietary Probiotic blend: 5 billons
Lactobacillus acidophilus
Bifidobacterium animalis subsp. lactis.
Other ingredients: Organic inulin fiber, stevia, natural orange flavor, citric acid, riboflavin Not a significant source of cholesterol, fat and protein
Nice to have
- We like simple design
Should not have
- Images from vintaro pictures.

```html
<!DOCTYPE html>
<html lang="en">
<head>
<meta charset="utf-8">
<title>Velquora Wraparound Label – Toskarend Nutrition</title>
<link rel="stylesheet" href="https://fonts.googleapis.com/css2?family=Merriweather:wght@900&family=Roboto:wght@700&family=Montserrat:wght@600&family=Roboto+Slab:wght@500&display=swap">
<style>
  :root {
    --page-bg: #e4e5e0;
    --label-green: #a3c548;
    --label-green-pale: #dbe6b8;
    --band-dark: #3a3a3c;
    --brand-blue: #2a9bd6;
    --ink: #1e1e1e;
    --white: #ffffff;
  }
  html, body {
    margin: 0;
    padding: 0;
    width: 1200px;
    height: 1200px;
    overflow: hidden;
    background: var(--page-bg);
  }
  /* 10.74 in × 2.87 in wraparound */
  .label {
    position: absolute;
    left: 20px;
    top: 445px;
    width: 1160px;
    height: 310px;
    background: var(--label-green);
  }
  .label-bands {
    position: absolute;
    inset: 0;
  }
  .front-panel {
    position: absolute;
    left: 380px;
    top: 0;
    width: 400px;
    height: 310px;
    text-align: center;
  }
  .brand-name {
    position: absolute;
    top: 40px;
    left: 0;
    width: 100%;
    margin: 0;
    font-family: "Merriweather", Georgia, serif;
    font-weight: 900;
    font-size: 17px;
    line-height: 20px;
    letter-spacing: -0.2px;
    color: var(--brand-blue);
  }
  .product-name {
    position: absolute;
    top: 62px;
    left: 0;
    width: 100%;
    margin: 0;
    font-family: "Merriweather", Georgia, serif;
    font-weight: 900;
    font-size: 24px;
    line-height: 28px;
    color: var(--ink);
  }
  .bacteria-badge {
    position: absolute;
    left: 127px;
    top: 98px;
    width: 146px;
    height: 50px;
    box-sizing: border-box;
    border: 2px solid var(--label-green-pale);
    font-family: "Roboto", Arial, sans-serif;
    font-weight: 700;
    line-height: 1;
  }
  .bacteria-count {
    height: 23px;
    background: var(--label-green);
    color: var(--white);
    font-size: 20px;
    padding-top: 2px;
    box-sizing: border-box;
  }
  .bacteria-label {
    height: 23px;
    background: var(--label-green-pale);
    color: var(--ink);
    font-size: 17px;
    padding-top: 3px;
    box-sizing: border-box;
  }
  .dose-lines {
    position: absolute;
    top: 155px;
    left: 0;
    width: 100%;
    font-family: "Montserrat", Arial, sans-serif;
    font-weight: 600;
    color: var(--ink);
  }
  .dose-lines p { margin: 0; font-size: 9.5px; line-height: 13px; }
  .dose-probiotic { letter-spacing: 1.6px; }
  .dose-prebiotic { letter-spacing: 0.5px; }
  .flavor-seal {
    position: absolute;
    left: 171px;
    top: 189px;
    width: 58px;
    height: 58px;
    box-sizing: border-box;
    border: 3px solid var(--white);
    border-radius: 50%;
    display: flex;
    align-items: center;
    justify-content: center;
    font-family: "Roboto Slab", Georgia, serif;
    font-weight: 500;
    font-size: 11px;
    line-height: 12px;
    color: var(--white);
  }
  .no-artificial {
    position: absolute;
    top: 253px;
    left: 0;
    width: 100%;
    margin: 0;
    font-family: "Montserrat", Arial, sans-serif;
    font-weight: 600;
    font-size: 8px;
    line-height: 12px;
    letter-spacing: 0.5px;
    color: var(--ink);
    font-variant: small-caps;
  }
  .no-artificial .initial { font-size: 10px; }
  .barcode-space {
    position: absolute;
    left: 960px;
    top: 160px;
    width: 140px;
    height: 90px;
    background: var(--white);
  }
</style>
</head>
<body>
  <section class="label" aria-label="Velquora wraparound label">
    <svg class="label-bands" width="1160" height="310" viewBox="0 0 1160 310" aria-hidden="true">
      <rect x="0" y="32" width="1160" height="94" fill="var(--label-green-pale)"/>
      <rect x="0" y="0" width="1160" height="15" fill="var(--band-dark)"/>
      <polygon points="495,14 665,14 580,38" fill="var(--band-dark)"/>
      <rect x="0" y="272" width="1160" height="15" fill="var(--band-dark)"/>
      <rect x="0" y="287" width="1160" height="23" fill="var(--white)"/>
      <polygon points="548,286 612,286 580,297" fill="var(--band-dark)"/>
    </svg>

    <div class="front-panel">
      <p class="brand-name">TOSKAREND NUTRITION</p>
      <h1 class="product-name">Velquora</h1>

      <div class="bacteria-badge">
        <div class="bacteria-count">100 BILLION</div>
        <div class="bacteria-label">LIVE BACTERIA</div>
      </div>

      <div class="dose-lines">
        <p class="dose-probiotic">5 GRAMS OF PROBIOTIC</p>
        <p class="dose-prebiotic">5 GRAMS OF PREBIOTIC</p>
      </div>

      <div class="flavor-seal">Orange<br>Flavor</div>

      <p class="no-artificial"><span class="initial">N</span>o artificial flavours</p>
    </div>

    <div class="barcode-space" role="img" aria-label="Space reserved for barcode"></div>
  </section>
</body>
</html>
```